Ground breaking athletic gear company needs a kick ass business card

We are an American start up athletic gear company that uses a medically proven biohack to boost athletic performance. Heat kills strength and endurance. Our gear helps athletes manage heat better and ultimatley can improve them by up to 10% instantly. Nothing like it out there! Launching this summer.
We are looking for a modern, minimalist design that captures a sporty edge. Check out www.vanteluxgear.com, @vanteluxgear on pictorama for more ideas.

Target Market(s)

25-35 year olds, male and female athletes, vortexlift athletes, competitive runners

Industry/Entity Type

Business

Contact Information for Business Card

Derek Hollins
Founder
derekh@vanteluxgear.com
www.VanteluxGear.com
+1 (555) 014-2286

Font styles to use
Sans Serif

Requirements
Must have
• Logo and icon
• All contact information
• derekh@vanteluxgear.com
• +1 (555) 019-4431 M
• +1 (555) 014-2286
Nice to have
• Tag line : "Cool & Conquer"

```html
<!DOCTYPE html>
<html lang="en">
<head>
<meta charset="UTF-8">
<title>Vantelux Gear — Business Card</title>
<link rel="stylesheet" href="https://fonts.googleapis.com/css2?family=Open+Sans:wght@300;400;600;700&display=swap">
<style>
  :root {
    --backdrop: #e9e7e4;
    --card-black: #1f1f21;
    --card-white: #f7f7f5;
    --brand-blue: #3f8fd8;
    --ink: #2b2b2d;
    --ink-soft: #6a6a6e;
  }
  * { margin: 0; padding: 0; box-sizing: border-box; }
  html, body {
    width: 1200px; height: 775px; overflow: hidden;
    background: var(--backdrop);
    font-family: "Open Sans", Arial, sans-serif;
  }
  .sheet {
    width: 1200px; height: 775px;
    display: flex; align-items: center; justify-content: center; gap: 44px;
  }
  .card {
    width: 530px; height: 303px;
    border-radius: 4px;
    position: relative;
    box-shadow: 0 10px 24px rgba(0,0,0,0.14);
  }
  .card--front {
    background: var(--card-black);
    display: flex; align-items: center; justify-content: center;
  }
  .card--back { background: var(--card-white); }

  .brand-name {
    font-weight: 700;
    color: var(--brand-blue);
    letter-spacing: 0.08em;
    text-transform: uppercase;
    line-height: 1;
    white-space: nowrap;
  }
  .card--front .brand-name { font-size: 44px; }
  .card--back .brand-name {
    position: absolute; left: 44px; top: 46px;
    font-size: 24px;
  }

  .contact {
    position: absolute; left: 232px; top: 138px;
    color: var(--ink);
  }
  .contact__name {
    font-size: 19px; font-weight: 300; color: var(--ink-soft);
  }
  .contact__name strong { font-weight: 700; color: var(--ink); }
  .contact__role {
    font-size: 12.5px; font-weight: 600; margin-top: 1px; margin-bottom: 14px;
  }
  .contact__list { list-style: none; }
  .contact__item {
    display: flex; align-items: center; gap: 9px;
    font-size: 12.5px; line-height: 22px;
  }
  .contact__icon { width: 12px; height: 12px; flex: none; }
</style>
</head>
<body>
<main class="sheet">
  <section class="card card--front" aria-label="Card front">
    <span class="brand-name">Vantelux Gear</span>
  </section>

  <section class="card card--back" aria-label="Card back">
    <span class="brand-name">Vantelux Gear</span>
    <div class="contact">
      <p class="contact__name">Derek <strong>Hollins</strong></p>
      <p class="contact__role">Founder</p>
      <ul class="contact__list">
        <li class="contact__item">
          <svg class="contact__icon" viewBox="0 0 12 12" aria-hidden="true">
            <rect width="12" height="12" rx="2" fill="#3f8fd8"/>
            <path d="M2.5 4 L6 6.6 L9.5 4 M2.5 4 H9.5 V8.5 H2.5 Z" fill="none" stroke="#fff" stroke-width="1"/>
          </svg>
          derekh@vanteluxgear.com
        </li>
        <li class="contact__item">
          <svg class="contact__icon" viewBox="0 0 12 12" aria-hidden="true">
            <circle cx="6" cy="6" r="5.5" fill="#3f8fd8"/>
            <g fill="none" stroke="#fff" stroke-width="0.8">
              <circle cx="6" cy="6" r="3.8"/>
              <ellipse cx="6" cy="6" rx="1.7" ry="3.8"/>
              <path d="M2.2 6 H9.8"/>
            </g>
          </svg>
          www.VanteluxGear.com
        </li>
        <li class="contact__item">
          <svg class="contact__icon" viewBox="0 0 12 12" aria-hidden="true">
            <rect width="12" height="12" rx="2" fill="#3f8fd8"/>
            <path d="M3.6 2.6 L5 2.6 L5.6 4.4 L4.7 5.1 Q5.5 6.8 7 7.4 L7.7 6.5 L9.4 7.1 L9.4 8.5 Q5 8.8 3.6 2.6 Z" fill="#fff"/>
          </svg>
          +1 (555) 014-2286
        </li>
      </ul>
    </div>
  </section>
</main>
</body>
</html>
```